hotel's Website

Hotels website redesign for reference pictures, logo etc see http://restwellmarlow.co.uk/

1. 2-3 Special offers on the main page.
2. Booking calender
3. Location Map
4. Picture gallery.
5. Journeyscope reviews.
6. short description
7. Social Media sharing.
8 Phone number and address.

Industry/Entity Type

Hotel

Requirements
Must have
• 1. 2-3 Special offers on the main page.
2. Booking calender
3. Location Map
4. Picture gallery.
5. Journeyscope reviews.
6. short description
7. Social Media sharing.

```html
<!DOCTYPE html>
<html lang="en">
<head>
<meta charset="utf-8">
<title>Restwell Inn London Victoria</title>
<link rel="stylesheet" href="https://fonts.googleapis.com/css2?family=Open+Sans:wght@400;600;700&display=swap">
<style>
:root{
  --blue:#1b609f;
  --blue-dark:#124a7c;
  --orange:#f7931e;
  --header:#1d1d1d;
  --footer:#2a2a2a;
  --footer-base:#1a1a1a;
  --grey-bg:#efefef;
  --text:#555;
  --muted:#8a8a8a;
  --white:#fff;
}
*{margin:0;padding:0;box-sizing:border-box}
html,body{width:695px;height:1200px;overflow:hidden}
body{font-family:"Open Sans",Arial,sans-serif;color:var(--text);background:var(--white);position:relative}
.abs{position:absolute}

/* Header */
.site-header{position:absolute;left:0;top:0;width:695px;height:70px;background:var(--header)}
.brand-mark{position:absolute;left:88px;top:6px;width:40px;height:40px;background:var(--blue);border:2px solid var(--white)}
.brand-name{position:absolute;left:74px;top:48px;font-size:7px;font-weight:600;color:var(--white);letter-spacing:.5px;white-space:nowrap}
.brand-name span{display:block;font-size:6px;color:#bbb;letter-spacing:1px}
.brand-location{position:absolute;left:139px;top:22px;font-size:10px;font-weight:600;color:var(--white)}
.brand-location b{color:var(--orange);font-weight:600}
.social-top{position:absolute;right:75px;top:5px;display:flex;gap:4px}
.social-top i,.social-foot i{display:block;border-radius:50%}
.social-top i{width:11px;height:11px}
.contact-line{position:absolute;right:75px;top:26px;font-size:7px;font-weight:600;color:var(--white)}
.translate{position:absolute;right:75px;top:47px;display:flex;align-items:center;gap:2px;background:#eee;padding:1px 3px;font-size:6px;color:#333}
.translate i{display:block;width:8px;height:6px;background:#999}

/* Nav */
.main-nav{position:absolute;left:0;top:70px;width:695px;height:29px;background:#f3f3f3;border-bottom:1px solid #ddd}
.main-nav ul{list-style:none;display:flex;position:absolute;left:84px;top:6px;gap:0}
.main-nav li{font-size:7.5px;font-weight:700;color:#333;padding:4px 11px;margin-right:10px;text-transform:uppercase}
.main-nav li.active{background:var(--blue);color:var(--white);border-radius:2px}

/* Hero */
.hero{position:absolute;left:0;top:99px;width:695px;height:228px;background:linear-gradient(180deg,#1e3b66 0%,#4b6d9b 38%,#7a6a7a 55%,#c77b3b 68%,#2b3346 80%,#17212f 100%)}
.intro{position:absolute;left:0;top:327px;width:695px;height:197px;background:var(--grey-bg)}

.card{position:absolute;top:304px;height:203px;background:var(--white);box-shadow:0 1px 3px rgba(0,0,0,.15)}
.card-icon{position:absolute;top:-25px;left:50%;margin-left:-26px;width:52px;height:52px;border-radius:50%;background:var(--blue);border:3px solid var(--white);display:flex;align-items:center;justify-content:center}
.card-label{position:absolute;left:-5px;bottom:6px;height:22px;background:var(--blue);color:var(--white);font-size:9.5px;padding:5px 0 0 21px;text-transform:uppercase}
.card-label::after{content:"";position:absolute;left:0;bottom:-5px;border-top:5px solid var(--blue-dark);border-left:5px solid transparent}
.card-text{position:absolute;top:41px;font-size:7.5px;line-height:11px;text-align:center;color:#666}
.card-photo{position:absolute;top:97px;height:66px}
.field-label{position:absolute;left:12px;font-size:7.5px;font-weight:600;color:#555}
.field{position:absolute;left:12px;width:140px;height:25px;border:1px solid #ddd;background:#f7f7f7;font-size:7px;color:#888;padding:7px 10px}
.btn-search{position:absolute;left:12px;top:130px;width:135px;height:28px;background:var(--orange);color:var(--white);font-size:9.5px;font-weight:700;text-align:center;line-height:28px;border-radius:2px}

/* Offers */
.section-title{position:absolute;font-size:14px;color:#444}
.offer{position:absolute;top:574px;width:120px;height:107px}
.offer-photo{height:80px}
.offer-info{height:27px;background:var(--blue);padding:3px 7px;color:var(--white);font-size:7px;line-height:10px}
.offer-info b{display:block;color:var(--orange);font-weight:700}
.arrow{position:absolute;top:611px;width:16px;height:16px;background:var(--blue-dark);display:flex;align-items:center;justify-content:center}

.info-band{position:absolute;left:0;top:710px;width:695px;height:270px;background:var(--grey-bg)}
.panel{position:absolute;top:759px;height:199px;background:var(--white);box-shadow:0 1px 3px rgba(0,0,0,.12)}
.map{position:absolute;left:6px;top:7px;width:154px;height:185px;background:linear-gradient(135deg,#e7e4dc,#d6d9d2)}
.review{position:absolute;left:12px;width:150px;font-size:7.5px;line-height:10.5px;color:#555}
.review h4{font-size:7.5px;color:var(--blue);font-weight:700;margin-bottom:2px}
.review time{display:block;color:var(--orange);font-size:6px;margin-top:3px}
.more-link{position:absolute;right:10px;bottom:9px;font-size:6.5px;color:var(--blue);font-weight:600;text-decoration:underline}
.thumbs{position:absolute;left:7px;top:8px;display:grid;grid-template-columns:repeat(3,44px);grid-auto-rows:43px;gap:9px 8px}
.thumbs i{display:block}
.gallery-bar{position:absolute;left:0;bottom:0;width:100%;height:38px;background:var(--blue);color:var(--white);font-size:10px;padding:13px 0 0 16px}

/* Footer */
.site-footer{position:absolute;left:0;top:980px;width:695px;height:181px;background:var(--footer);color:#bbb}
.footer-col{position:absolute;top:13px}
.footer-col h3{font-size:12.5px;font-weight:400;color:var(--white);margin-bottom:12px}
.footer-col ul{list-style:none;font-size:7px;line-height:14px;text-transform:uppercase}
.footer-col p{font-size:7px;line-height:13px;color:#aaa}
.partner-links{list-style:none;margin-top:8px;font-size:7.5px;line-height:14px}
.partner-links li{color:var(--orange);text-decoration:underline;text-transform:none}
.email{width:172px;height:25px;background:#9a9a9a;color:#333;font-size:7px;padding:8px 8px;margin-top:17px}
.subscribe{width:67px;height:22px;background:var(--blue);color:var(--white);font-size:7px;font-weight:700;text-align:center;line-height:22px;margin-top:11px}
.footer-base{position:absolute;left:0;top:1161px;width:695px;height:39px;background:var(--footer-base)}
.copyright{position:absolute;left:74px;top:14px;font-size:7px;color:#888}
.social-foot{position:absolute;right:74px;top:11px;display:flex;gap:4px}
.social-foot i{width:17px;height:17px}
</style>
</head>
<body>

<header class="site-header">
  <div class="brand-mark"></div>
  <div class="brand-name">RESTWELL INN<span>BY MARLOW HEARTH HOTELS</span></div>
  <div class="brand-location">London - <b>Victoria</b></div>
  <div class="social-top">
    <i style="background:#3b5b98"></i><i style="background:#29a9e1"></i><i style="background:#d8422f"></i><i style="background:#c4302b"></i>
  </div>
  <div class="contact-line">Call : +44 (0) 20 7946 0102 &nbsp;|&nbsp; Fax : +44 (0) 20 7946 0187</div>
  <div class="translate"><i></i><i></i><span>TRANSLATE</span><i></i></div>
</header>

<nav class="main-nav">
  <ul>
    <li class="active">Home</li><li>Our Rooms</li><li>Attractions</li><li>London Events</li><li>Special Offers</li><li>Photos</li><li>Directions</li><li>Contact</li>
  </ul>
</nav>

<div class="hero" role="img" aria-label="Evening view of the Thames with the observation wheel and Westminster lit up"></div>
<div class="intro"></div>

<section class="card" style="left:73px;width:167px">
  <div class="card-icon">
    <svg width="20" height="20" viewBox="0 0 20 20" fill="none" stroke="#fff" stroke-width="1.6"><rect x="2" y="4" width="16" height="14" rx="1"/><path d="M2 8h16M6 2v4M14 2v4"/><path d="M6 11h2M10 11h2M14 11h1M6 14h2M10 14h2" stroke-width="1.3"/></svg>
  </div>
  <div class="field-label" style="top:33px">From</div>
  <div class="field" style="top:46px">November 04, 2013</div>
  <div class="field-label" style="top:79px">To</div>
  <div class="field" style="top:91px">November 04, 2013</div>
  <div class="btn-search">SEARCH AVAILABILTY</div>
  <div class="card-label" style="width:161px">Book your room</div>
</section>

<section class="card" style="left:263px;width:167px">
  <div class="card-icon">
    <svg width="22" height="14" viewBox="0 0 22 14" fill="none" stroke="#fff" stroke-width="1.6"><path d="M1 7C5 1 17 1 21 7C17 13 5 13 1 7Z"/><circle cx="11" cy="7" r="3"/></svg>
  </div>
  <p class="card-text" style="left:12px;width:143px">London is one of the culture capitals of the world and is brimming with exciting things to see and do. Come and stay at the Restwell Inn Victoria to experience it!</p>
  <div class="card-photo" role="img" aria-label="Photo of a London palace facade" style="left:11px;width:145px;background:linear-gradient(180deg,#b9c6d3,#8e8a7c 60%,#6d6a5e)"></div>
  <div class="card-label" style="width:166px">Explore London</div>
</section>

<section class="card" style="left:455px;width:165px">
  <div class="card-icon">
    <svg width="22" height="16" viewBox="0 0 22 16" fill="none" stroke="#fff" stroke-width="1.6"><path d="M2 2v13M2 11h18v4M2 8h18v3"/><rect x="4" y="4" width="5" height="4" rx="1"/></svg>
  </div>
  <p class="card-text" style="left:10px;width:145px;text-align:justify">If you're looking for a hotel near many of London's most popular attractions Restwell Inn Victoria is one of the best options to choose from as the hotel offer the convenient accommodation at an affordable price.</p>
  <div class="card-photo" role="img" aria-label="Photo of a bright hotel lounge with colourful chairs" style="left:9px;width:145px;background:linear-gradient(135deg,#c8b26a,#d84d3a 50%,#3c6fb0)"></div>
  <div class="card-label" style="width:166px">Stay in comfort</div>
</section>

<h2 class="section-title" style="left:77px;top:537px">Special Offers</h2>
<div class="arrow" style="left:74px"><svg width="6" height="8" viewBox="0 0 6 8"><path d="M5 0L1 4L5 8" fill="none" stroke="#fff" stroke-width="1.6"/></svg></div>
<div class="arrow" style="left:603px"><svg width="6" height="8" viewBox="0 0 6 8"><path d="M1 0L5 4L1 8" fill="none" stroke="#fff" stroke-width="1.6"/></svg></div>

<article class="offer" style="left:80px"><div class="offer-photo" role="img" aria-label="Photo of the hotel coffee station" style="background:linear-gradient(180deg,#5d5a54,#8c8270 60%,#3a342c)"></div><div class="offer-info">Place Name<b>Save up to 30 %</b></div></article>
<article class="offer" style="left:215px"><div class="offer-photo" role="img" aria-label="Photo of the hotel coffee station" style="background:linear-gradient(180deg,#5d5a54,#8c8270 60%,#3a342c)"></div><div class="offer-info">Place Name<b>Save up to 30 %</b></div></article>
<article class="offer" style="left:351px"><div class="offer-photo" role="img" aria-label="Photo of a warm-toned hotel room" style="background:linear-gradient(180deg,#d8b98a,#a5703f 60%,#6b4a2c)"></div><div class="offer-info">Place Name<b>Save up to 30 %</b></div></article>
<article class="offer" style="left:488px"><div class="offer-photo" role="img" aria-label="Photo of a hotel bedroom with red bedding" style="background:linear-gradient(180deg,#e0c9a6,#c27556 55%,#8e2f2a)"></div><div class="offer-info">Place Name<b>Save up to 30 %</b></div></article>

<div class="info-band"></div>
<h2 class="section-title" style="left:113px;top:727px">Location Map</h2>
<h2 class="section-title" style="left:283px;top:727px">Journeyscope Reviews</h2>
<h2 class="section-title" style="left:495px;top:727px">Picture Gallery</h2>

<section class="panel" style="left:73px;width:166px">
  <div class="map" role="img" aria-label="Street map showing the hotel location near London Victoria"></div>
  <svg class="abs" style="left:67px;top:68px" width="14" height="20" viewBox="0 0 14 20"><path d="M7 19C7 19 1 11 1 7A6 6 0 0 1 13 7C13 11 7 19 7 19Z" fill="#d9342b"/><circle cx="7" cy="7" r="2.2" fill="#fff"/></svg>
</section>

<section class="panel" style="left:260px;width:166px">
  <div class="review" style="top:12px"><h4>Place Name</h4>" Enjoy your stay at Restwell Inn Victoria and be sure that you've found our best value on the Internet. "<time>02 November 2013</time></div>
  <div class="review" style="top:74px"><h4>Place Name</h4>Bethat you've found our best value on the Internet. "<time>02 November 2013</time></div>
  <div class="review" style="top:126px"><h4>Place Name</h4>" Enjoy your stay at Restwell Inn Victoria and be sure that you've found"<time>02 November 2013</time></div>
  <div class="more-link">More reviews</div>
</section>

<section class="panel" style="left:455px;width:167px">
  <div class="thumbs" role="img" aria-label="Gallery of hotel room and lounge photos">
    <i style="background:#b27a4a"></i><i style="background:#c9a27a"></i><i style="background:#a65b3c"></i>
    <i style="background:#6a6258"></i><i style="background:#8b9bb0"></i><i style="background:#c0894f"></i>
    <i style="background:#c56a44"></i><i style="background:#d8b27e"></i><i style="background:#9c5a3a"></i>
  </div>
  <div class="gallery-bar">MORE IMAGES</div>
</section>

<footer class="site-footer">
  <div class="footer-col" style="left:73px">
    <h3>Quick Links</h3>
    <ul><li>Home</li><li>Our Rooms</li><li>Attractions</li><li>London Events</li><li>Special Offers</li><li>Photos</li><li>Directions</li><li>Contact</li></ul>
  </div>
  <div class="footer-col" style="left:231px;width:150px">
    <h3>Partner Hotels</h3>
    <p>This hotel is owned and operated by the Linden Hotel Group, please take a look of some of our other hotels below:</p>
    <ul class="partner-links">
      <li>Harbourside Lodge - Camden Lock</li><li>Harbourside Express - Earls Court</li><li>Meridian House Hotel</li><li>Simplestay Victoria</li><li>Restwell Suites - King's Cross</li>
    </ul>
  </div>
  <div class="footer-col" style="left:447px;width:180px">
    <h3>Stay in Touch</h3>
    <p>Sign up for our newsletter for latest news from Restwell Inn London - Victoria</p>
    <div class="email">Enter Your Email address</div>
    <div class="subscribe">SUBSCRIBE</div>
  </div>
</footer>
<div class="footer-base">
  <div class="copyright">© 2013. All rights reserved.</div>
  <div class="social-foot"><i style="background:#2d6db5"></i><i style="background:#29a9e1"></i><i style="background:#d8422f"></i><i style="background:#c4302b"></i></div>
</div>

</body>
</html>
```